Lead Generating Website Design

We are looking for a brand new design for our existing website.
The existing website is www.brvpartnerhub.com
The website is aimed at businesses that would like to licence the courses from our school to sell themselves.
We want the menu to be the following:
* Home
* About us
* Our Courses
* LMS Platform
* Affiliate Program
* Contact Us
We want the colour scheme to use the following design guide:
https://docvault.example/pedalforward/docs/keen_to_cycle_brand_guidelines
Like the idea of the circles and colours in the style guide for places. Want lots of white areas as well as coloured areas
An example of a nice looking site is : https://www.studyharbour.online/
MUST look good on mobile also
On the home page we want the following:
A large image with the text :
Over 450 courses written by highly qualified academics with real world experience.
The 'Join our thriving group of Affiliates - start your own online college!' section on the current website with the text and becoming an affiliate video
A section for 'see how our LMS works' with some text and a place for a video
A section for 'About BRV Remote Learning' with the text BRV Remote Learning has been providing distance education for over 40 years and have been the leader in online education for over 25 years.
Benefit from the resources and experience of one of the worlds leading course content providers.
Our highly qualified academic staff, HUGE resource library of up to date courses and cutting edge white label LMS enable our affiliates to stay well ahead of their competitors
A section for 'Free information pack' like the one on https://www.studyharbour.online/
Target Market(s)
Education providers looking to licence our courses to sell
Number of Pages Required
1 page

```html
<!DOCTYPE html>
<html lang="en">
<head>
<meta charset="utf-8">
<title>BRV Remote Learning – Affiliates</title>
<link href="https://fonts.googleapis.com/css2?family=Playfair+Display:wght@400;700&family=Roboto:wght@400;500;700&display=swap" rel="stylesheet">
<style>
  :root{
    --blue:#1d4fb8;
    --navy:#15264a;
    --red:#e9434b;
    --teal:#27a3a5;
    --orange:#f2a431;
    --ink:#2b2f38;
    --grey:#777c86;
    --white:#ffffff;
    --serif:'Playfair Display', Georgia, serif;
    --sans:'Roboto', Arial, sans-serif;
  }
  *{box-sizing:border-box;margin:0;padding:0}
  html,body{width:1200px;height:3496px;overflow:hidden;background:var(--white)}
  body{position:relative;font-family:var(--sans);color:var(--ink)}
  .abs{position:absolute}

  /* header */
  .site-header{left:0;top:0;width:1200px;height:52px;background:var(--white);z-index:3}
  .brand{left:144px;top:12px;display:flex;align-items:center;gap:8px;font:500 15px/1 var(--sans);color:var(--blue)}
  .brand-mark{width:22px;height:22px;background:var(--blue)}
  .main-nav{right:128px;top:14px;display:flex;gap:6px}
  .main-nav a{font:500 14px/24px var(--sans);color:var(--navy);text-decoration:none;padding:0 10px}
  .main-nav a.current{background:var(--blue);color:var(--white)}

  /* hero */
  .hero{left:0;top:52px;width:1200px;height:600px;background:linear-gradient(100deg,#1b2d55 0%,#223d73 45%,#2f5a96 75%,#5b82b8 100%)}
  .hero-title{left:144px;top:110px;width:560px;font:400 46px/58px var(--serif);color:var(--white);text-transform:uppercase}
  .btn-outline{display:flex;align-items:center;justify-content:center;border:2px solid var(--white);color:var(--white);font:500 13px/1 var(--sans);text-transform:uppercase;letter-spacing:.5px}
  .hero .btn-outline{left:144px;top:396px;width:152px;height:44px}
  .slider-dots{right:44px;top:300px;display:flex;flex-direction:column;gap:12px}
  .slider-dots span{width:7px;height:7px;border-radius:50%;background:var(--white)}

  .video{width:656px;height:360px;left:272px}
  .video-play{left:50%;top:50%;width:74px;height:74px;margin:-37px 0 0 -37px}

  /* affiliates */
  .section-title{left:0;width:1200px;text-align:center;font:400 44px/56px var(--serif);color:var(--ink)}
  .affiliates-title{top:948px}
  .affiliates-lead{left:0;top:1050px;width:1200px;text-align:center;font:500 18px/26px var(--sans);color:var(--blue)}
  .affiliates-text{left:300px;top:1140px;width:600px;text-align:center;font:400 12px/19px var(--sans);color:var(--grey)}
  .btn-blue{left:526px;top:1234px;width:148px;height:44px;display:flex;align-items:center;justify-content:center;border:2px solid var(--blue);color:var(--blue);font:500 13px/1 var(--sans);text-transform:uppercase}

  /* LMS */
  .lms-band{left:0;top:1190px;width:1200px;height:1020px}
  .lms-title{left:0;top:1772px;width:1200px;text-align:center;font:700 38px/48px var(--serif);color:var(--white);text-transform:uppercase;letter-spacing:2px}
  .lms-text{left:290px;top:1846px;width:620px;text-align:center;font:400 12px/19px var(--sans);color:#fde6e7}
  .lms .btn-outline{left:526px;top:2014px;width:148px;height:44px}

  /* about */
  .about-title{top:2222px}
  .about-text{left:270px;top:2310px;width:660px;text-align:center;font:400 13px/20px var(--sans);color:var(--grey)}
  .features{left:0;top:2448px;width:1200px;display:flex;justify-content:center;gap:112px}
  .feature{width:176px;text-align:center}
  .feature-icon{width:176px;height:176px}
  .feature h3{margin-top:18px;font:700 20px/26px var(--sans);color:var(--blue)}

  /* info pack */
  .pack-band{left:0;top:2720px;width:1200px;height:700px}
  .pack-title{left:0;top:2932px;width:1200px;text-align:center;font:400 42px/54px var(--serif);color:var(--white);letter-spacing:2px}
  .pack-form{left:320px;top:3034px;width:560px}
  .field-row{display:flex;gap:16px;margin-bottom:16px}
  .field{flex:1;height:42px;background:var(--white);font:400 12px/42px var(--sans);color:#8a8f98;padding-left:12px}
  .pack-form .btn-outline{width:152px;height:44px;margin:24px auto 0}

  /* footer */
  .site-footer{left:0;top:3420px;width:1200px;height:76px;background:var(--white)}
  .copyright{left:144px;top:30px;font:400 12px/16px var(--sans);color:var(--grey)}
  .social{right:136px;top:22px;display:flex;gap:10px}
  .social span{width:30px;height:30px;border-radius:50%;background:var(--red)}
  .social span:first-child{background:var(--blue)}
  .page-num{right:16px;top:58px;font:400 10px/1 var(--sans);color:var(--grey)}
</style>
</head>
<body>

<header class="site-header abs">
  <div class="brand abs"><span class="brand-mark"></span>BRV Remote Learning</div>
  <nav class="main-nav abs">
    <a class="current" href="#">Home</a>
    <a href="#">About us</a>
    <a href="#">Our Courses</a>
    <a href="#">LMS Platform</a>
    <a href="#">Affiliate Program</a>
    <a href="#">Contact Us</a>
  </nav>
</header>

<section class="hero abs" role="img" aria-label="Photo of a learner working at a laptop, dark blue tones">
  <h1 class="hero-title abs">Over 450 courses written by highly qualified academics with real world experience.</h1>
  <a class="btn-outline abs" href="#">Get Started</a>
  <div class="slider-dots abs"><span></span><span></span><span></span><span></span></div>
</section>

<div class="video abs" style="top:540px;z-index:2;background:linear-gradient(120deg,#6b7f99 0%,#a9b3bf 45%,#3d3a3c 80%,#1e1c1e 100%)" role="img" aria-label="Affiliate video still showing two presenters beside a course licence slide">
  <svg class="video-play abs" viewBox="0 0 74 74"><circle cx="37" cy="37" r="34" fill="none" stroke="#fff" stroke-width="3"/><path d="M30 24 L52 37 L30 50 Z" fill="#fff"/></svg>
</div>

<section class="affiliates">
  <h2 class="section-title affiliates-title abs">Join our thriving group<br>of Affiliates</h2>
  <p class="affiliates-lead abs">Start your own online college' section on the current website<br>with the text and becoming an affiliate video</p>
  <p class="affiliates-text abs">You might already be working in education, or perhaps you're part of an association that is looking to expand it's offerings to it's members, or just a motivated business person!</p>
  <a class="btn-blue abs" href="#">Read More</a>
</section>

<section class="lms">
  <svg class="lms-band abs" viewBox="0 0 1200 1020" preserveAspectRatio="none">
    <polygon points="0,200 1200,0 1200,1000 0,940" fill="var(--red)"/>
  </svg>
  <div class="video abs" style="top:1368px;background:linear-gradient(120deg,#4d6a8a 0%,#7e93a8 40%,#b9c2cb 70%,#5e7088 100%)" role="img" aria-label="LMS walkthrough video still with a presenter in an office">
    <svg class="video-play abs" viewBox="0 0 74 74"><circle cx="37" cy="37" r="34" fill="none" stroke="#fff" stroke-width="3"/><path d="M30 24 L52 37 L30 50 Z" fill="#fff"/></svg>
  </div>
  <h2 class="lms-title abs">See how our LMS works</h2>
  <p class="lms-text abs">Established in 1979, the leading distance education provider offers hundreds of courses through a modern learning platform built for partners. Affiliates can brand the system, enrol students, track progress and issue certificates, all from one simple dashboard that works on any device.</p>
  <a class="btn-outline abs" href="#">Read More</a>
</section>

<section class="about">
  <h2 class="section-title about-title abs">About BRV Remote Learning</h2>
  <p class="about-text abs">BRV Remote Learning has been providing distance education for over 40 years and have been the leader in online education for over 25 years. Benefit from the resources and experience of one of the worlds leading course content providers. Our highly qualified academic staff, HUGE resource library of up to date courses and cutting edge white label LMS enable our affiliates to stay well ahead of their competitors.</p>
  <div class="features abs">
    <div class="feature">
      <svg class="feature-icon" viewBox="0 0 176 176"><circle cx="88" cy="88" r="84" fill="none" stroke="var(--orange)" stroke-width="4"/><rect x="50" y="56" width="76" height="50" rx="3" fill="none" stroke="var(--blue)" stroke-width="3"/><path d="M78 106 L74 120 H102 L98 106 M66 120 H110" fill="none" stroke="var(--blue)" stroke-width="3"/><path d="M70 80 L88 70 L106 80 L88 90 Z" fill="var(--orange)"/></svg>
      <h3>Delivering our courses</h3>
    </div>
    <div class="feature">
      <svg class="feature-icon" viewBox="0 0 176 176"><circle cx="88" cy="88" r="84" fill="none" stroke="var(--orange)" stroke-width="4"/><rect x="60" y="46" width="56" height="80" rx="3" fill="none" stroke="var(--blue)" stroke-width="3"/><path d="M70 64 H106 M70 76 H106 M70 88 H96" stroke="var(--orange)" stroke-width="3"/><circle cx="88" cy="114" r="4" fill="var(--blue)"/></svg>
      <h3>Selling our ebooks</h3>
    </div>
    <div class="feature">
      <svg class="feature-icon" viewBox="0 0 176 176"><circle cx="88" cy="88" r="84" fill="none" stroke="var(--orange)" stroke-width="4"/><path d="M58 92 V82 A30 30 0 0 1 118 82 V92" fill="none" stroke="var(--blue)" stroke-width="3"/><rect x="52" y="88" width="14" height="24" rx="4" fill="var(--orange)"/><rect x="110" y="88" width="14" height="24" rx="4" fill="var(--orange)"/><path d="M117 112 Q117 128 96 128" fill="none" stroke="var(--blue)" stroke-width="3"/><path d="M70 140 Q88 118 106 140" fill="none" stroke="var(--blue)" stroke-width="3"/></svg>
      <h3>Extra support available</h3>
    </div>
  </div>
</section>

<section class="pack">
  <svg class="pack-band abs" viewBox="0 0 1200 700" preserveAspectRatio="none" role="img" aria-label="Teal tinted photo of hands typing on a laptop">
    <defs><linearGradient id="packFill" x1="0" y1="0" x2="1" y2="1"><stop offset="0" stop-color="#3bb6b4"/><stop offset=".55" stop-color="#27a3a5"/><stop offset="1" stop-color="#7fcdcc"/></linearGradient></defs>
    <polygon points="0,60 1200,0 1200,700 0,700" fill="url(#packFill)"/>
  </svg>
  <h2 class="pack-title abs">Free information pack</h2>
  <form class="pack-form abs">
    <div class="field-row"><div class="field">Enter Name</div><div class="field">Enter Email</div></div>
    <div class="field-row"><div class="field">Send me the Pack</div></div>
    <div class="field-row"><div class="field">Phone</div></div>
    <div class="btn-outline">Submit</div>
  </form>
</section>

<footer class="site-footer abs">
  <p class="copyright abs">Copyright © 2021 BRV Remote Learning All Rights Reserved &nbsp;|&nbsp; Privacy policy &nbsp;|&nbsp; Terms and use</p>
  <div class="social abs" aria-label="Social links"><span></span><span></span><span></span><span></span></div>
  <span class="page-num abs">04</span>
</footer>

</body>
</html>
```